Book Cover Design Project

We need a book cover for a eBook on internet banking.

This eBook is meant to be an easy to read, practical book to help people understand what internet banking is, the pros and cons and cover the pure 'internet only' banks that have no branches. The intention is to help people to make informed decisions about whether to use internet banking, how to use it safely and explain in detail what 'internet only' banks are and whether they are right for them.

The cover should not look technical so that non-technical people are not scared off by the look. I have uploaded a book cover design that has the style that I am trying to portray, I have also uploaded a front cover that I created but do not think is suitable.

The cover wording layout could be something like
"Internet Banking"
"A practical guide to answer all your questions" or "The ultimate guide to internet banking" or "The Who's What's and How's of Internet Banking"
Authors name : Colin Pettifer

Industry/Entity Type

Internet

```html
<!DOCTYPE html>
<html lang="en">
<head>
<meta charset="utf-8">
<title>Internet Banking – Cover Options</title>
<link href="https://fonts.googleapis.com/css2?family=Oswald:wght@500;600&family=PT+Serif&display=swap" rel="stylesheet">
<style>
  :root {
    --page-bg: #eeeeea;
    --cover-frame: #ffffff;
    --navy-top: #0e2a5c;
    --navy-mid: #1a3f7e;
    --navy-deep: #0a1f47;
    --navy-key: #2a4f8f;
    --teal-band: rgba(63,164,201,0.55);
    --globe-light: #c9d5e6;
    --globe-mid: #7f97bd;
    --sky-top: #29aee0;
    --sky-bottom: #1c9fd6;
    --panel-blue: #1a82bd;
    --panel-dark: #1370a8;
    --text-white: #ffffff;
    --text-soft: #e3f2fb;
  }
  * { margin: 0; padding: 0; box-sizing: border-box; }
  html, body {
    width: 900px; height: 1200px; overflow: hidden;
    background: var(--page-bg);
  }
  .cover-pair {
    position: absolute; top: 331px; left: 40px;
    display: flex; gap: 60px;
  }
  .book-cover {
    position: relative;
    width: 380px; height: 538px;
    border: 8px solid var(--cover-frame);
    box-shadow: 0 4px 14px rgba(0,0,0,0.25);
    overflow: hidden;
    color: var(--text-white);
    text-align: center;
  }
  .book-cover--navy {
    background: radial-gradient(ellipse at 50% 45%, var(--navy-mid) 0%, var(--navy-top) 55%, var(--navy-deep) 100%);
  }
  .book-cover--sky {
    background: linear-gradient(180deg, var(--sky-top), var(--sky-bottom));
  }
  .top-band {
    position: absolute; left: 0; right: 0; top: 0; height: 80px;
    background: linear-gradient(180deg, var(--teal-band), rgba(63,164,201,0));
  }
  .cover-title {
    position: relative;
    font-family: "Oswald", sans-serif;
    font-weight: 600;
    font-size: 66px;
    line-height: 0.98;
    letter-spacing: -0.5px;
    text-transform: uppercase;
    padding-top: 50px;
  }
  .cover-subtitle {
    position: relative;
    font-family: "PT Serif", serif;
    font-size: 15px;
    margin-top: 8px;
    color: var(--text-soft);
  }
  .globe-area {
    position: absolute; left: 100px; top: 245px;
    width: 165px; height: 165px;
    border-radius: 10px;
    background: linear-gradient(160deg, var(--globe-light), var(--globe-mid));
    opacity: 0.85;
  }
  .keys-area {
    position: absolute; left: 0; right: 0; bottom: 0; height: 190px;
    background: linear-gradient(180deg, rgba(42,79,143,0) 0%, var(--navy-key) 45%, var(--navy-deep) 100%);
  }
  .signin-area {
    position: absolute; left: 86px; top: 236px;
    width: 208px; height: 108px;
    border-radius: 8px;
    background: linear-gradient(180deg, var(--panel-blue), var(--panel-dark));
  }
  .author {
    position: absolute; left: 0; right: 0; bottom: 26px;
    font-family: "Oswald", sans-serif;
    font-weight: 500;
    font-size: 32px;
    letter-spacing: 0.5px;
    text-transform: uppercase;
  }
</style>
</head>
<body>
  <main class="cover-pair">
    <section class="book-cover book-cover--navy">
      <div class="top-band" role="img" aria-label="Band of teal dots across the top of the cover"></div>
      <div class="keys-area" role="img" aria-label="Rows of dark blue keyboard keys fading up from the bottom"></div>
      <div class="globe-area" role="img" aria-label="Illustration of a white globe showing the continents"></div>
      <h1 class="cover-title">Internet<br>Banking</h1>
      <p class="cover-subtitle">The ultimate guide to internet banking</p>
      <p class="author">Colin Pettifer</p>
    </section>

    <section class="book-cover book-cover--sky">
      <h1 class="cover-title">Internet<br>Banking</h1>
      <p class="cover-subtitle">The ultimate guide to internet banking</p>
      <div class="signin-area" role="img" aria-label="Illustration of an online banking sign-in box with username and password fields"></div>
      <p class="author">Colin Pettifer</p>
    </section>
  </main>
</body>
</html>
```